We are a new towing and recovery company starting out in Calhan, CO. We do not want anything generic, we are looking to stand out. we will be doing towing for motorcycles to straight trucks we will have a rollback a 16-ton wrecker and a service vehicle with a wheel lift attached to tow small sized vehicles. We will also be doing roadside services which include lock-out, fuel delivery, jumpstarts, tire changes, and minor auto repair. we will be providing a quality and fast service also customer service will be one of main focuses.

Contact Information for Business Card

Brindle Towing and Recovery, Gus Lindqvist, Owner, 48213 S. Orrin Road, Orrin Flats, CO 80899 719-562-9147 Phone 719-562-9288 Fax www.brindletowingandrecovery.example

```html
<!DOCTYPE html>
<html lang="en">
<head>
<meta charset="utf-8">
<title>Brindle Towing and Recovery – Business Card</title>
<link rel="stylesheet" href="https://fonts.googleapis.com/css2?family=Arimo:wght@400;700&family=Russo+One&display=swap">
<style>
  :root {
    --page-bg: #eef0f3;
    --card-white: #ffffff;
    --brand-navy: #24397f;
    --navy-light: #2f4a9c;
    --navy-dark: #17245c;
    --brand-red: #d8262c;
    --name-red: #e8453f;
    --text-white: #ffffff;
    --divider: rgba(255,255,255,0.55);
    --truck-white: #e9edf3;
    --truck-yellow: #f2d23a;
    --truck-blue: #3f7fcf;
  }
  * { box-sizing: border-box; margin: 0; padding: 0; }
  html, body {
    width: 1200px; height: 900px; overflow: hidden;
    background: var(--page-bg);
  }
  .card {
    position: absolute; left: 100px; top: 164px;
    width: 1000px; height: 572px;
    border-radius: 34px; overflow: hidden;
    background: var(--card-white);
    box-shadow: 0 18px 40px rgba(20,30,60,0.18);
  }
  .brand-name {
    position: absolute; left: 0; right: 0; top: 38px;
    text-align: center;
    font-family: "Arimo", Arial, sans-serif;
    font-weight: 700;
    font-size: 54px; line-height: 1;
    color: var(--brand-navy);
  }
  .fleet-illustration {
    position: absolute; left: 240px; top: 122px;
    width: 520px; height: 188px;
    border-radius: 14px;
    background: linear-gradient(90deg, var(--truck-white) 0%, #cfd7e3 45%, var(--truck-blue) 55%, var(--truck-yellow) 72%, #c9ccd2 100%);
  }
  .tagline-band {
    position: absolute; left: 0; right: 0; top: 318px; height: 34px;
    background: var(--brand-red);
    display: flex; align-items: center; justify-content: center;
  }
  .tagline {
    font-family: "Russo One", Arial, sans-serif;
    font-size: 25px; letter-spacing: 5px;
    color: var(--navy-dark);
  }
  .contact-panel {
    position: absolute; left: 0; right: 0; top: 352px; bottom: 0;
    background: linear-gradient(180deg, var(--navy-light) 0%, var(--brand-navy) 45%, var(--navy-dark) 100%);
    font-family: "Arimo", Arial, sans-serif;
    color: var(--text-white);
  }
  .owner { position: absolute; left: 60px; top: 28px; }
  .owner-name { font-size: 28px; color: var(--name-red); }
  .owner-title { font-size: 23px; margin-top: 6px; }
  .divider {
    position: absolute; left: 300px; top: 16px; bottom: 30px;
    width: 2px; background: var(--divider);
  }
  .contact-list {
    position: absolute; left: 318px; top: 16px;
    list-style: none; font-size: 22px; line-height: 26px;
  }
  .contact-list li { display: flex; align-items: center; gap: 6px; }
  .contact-list .continued { padding-left: 28px; }
  .icon { width: 22px; height: 22px; flex: none; }
</style>
</head>
<body>
  <div class="card">
    <div class="brand-name">Brindle Towing and Recovery</div>
    <div class="fleet-illustration" role="img" aria-label="Illustration of a white wrecker tow truck and a yellow rollback truck"></div>
    <div class="tagline-band"><span class="tagline">ANY LOAD, ANY ROAD, ANY TIME</span></div>
    <div class="contact-panel">
      <div class="owner">
        <div class="owner-name">Gus Lindqvist</div>
        <div class="owner-title">Owner/Operator</div>
      </div>
      <div class="divider"></div>
      <ul class="contact-list">
        <li>
          <svg class="icon" viewBox="0 0 24 24" aria-hidden="true"><rect x="7" y="2" width="10" height="20" rx="2" fill="none" stroke="var(--brand-red)" stroke-width="2"/><circle cx="12" cy="18.5" r="1.2" fill="var(--brand-red)"/></svg>
          719-562-9030
        </li>
        <li>
          <svg class="icon" viewBox="0 0 24 24" aria-hidden="true"><path d="M6 3l4 4-2 3c1.5 3 3 4.5 6 6l3-2 4 4-3 3C10 20 4 14 3 6z" fill="var(--brand-red)"/></svg>
          719-562-9147
        </li>
        <li>
          <svg class="icon" viewBox="0 0 24 24" aria-hidden="true"><rect x="3" y="9" width="18" height="11" rx="2" fill="var(--brand-red)"/><rect x="7" y="3" width="10" height="7" fill="none" stroke="var(--brand-red)" stroke-width="2"/><rect x="7" y="13" width="10" height="2" fill="var(--text-white)"/></svg>
          719-562-9288
        </li>
        <li>
          <svg class="icon" viewBox="0 0 24 24" aria-hidden="true"><rect x="3" y="6" width="18" height="13" rx="1.5" fill="var(--brand-red)"/><path d="M3 7l9 7 9-7" fill="none" stroke="var(--text-white)" stroke-width="1.6"/></svg>
          brindle_towing@mailbox.example
        </li>
        <li>
          <svg class="icon" viewBox="0 0 24 24" aria-hidden="true"><circle cx="12" cy="12" r="9" fill="none" stroke="var(--brand-red)" stroke-width="2"/><ellipse cx="12" cy="12" rx="4" ry="9" fill="none" stroke="var(--brand-red)" stroke-width="1.6"/><path d="M3 12h18" stroke="var(--brand-red)" stroke-width="1.6"/></svg>
          www.brindletowingandrecovery.example
        </li>
        <li>
          <svg class="icon" viewBox="0 0 24 24" aria-hidden="true"><path d="M2 12L12 3l10 9h-3v9h-5v-6h-4v6H5v-9z" fill="var(--brand-red)"/></svg>
          48213 S. Orrin Road,
        </li>
        <li class="continued">Orrin Flats, CO 80899</li>
      </ul>
    </div>
  </div>
</body>
</html>
```